Design Invitation using a mobile phone screen image

This invitation is for 12 year olds finishing primary school so make it fun and bright.
Invitation should be an kavrel with a text message saying.....
Dress in your best (insert emoticons - boy in long pants/girl in dress) for your Year 6 farewell dinner (insert emoticon with tear) on Monday 12 December at 6 pm (insert emoticons - party hat, thumbs up and bowl of icecream). Going 2b a gr8 night!
rsvp YES PLEASE and your name to 0459XXXXXXX

Target Market(s)

12/13 years old boys and girls

Industry/Entity Type

School

Requirements
Must have
• Must be bright and look like a text message - it can have an artwork within it as if the invite has been texted and then a comment is made after the image.
• Must us an kavrel screen as the invitation but so we dont have to cut it out it can be a rectanglar card

```html
<!DOCTYPE html>
<html lang="en">
<head>
<meta charset="utf-8">
<title>Year 6 Farewell Dinner Invitation</title>
<link href="https://fonts.googleapis.com/css2?family=Jost:wght@500;600;700&family=Great+Vibes&display=swap" rel="stylesheet">
<style>
  :root {
    --stage: #e6e6e6;
    --ink: #1a1a1a;
    --red: #e4262b;
    --gold: #b8862b;
    --gold-band: #c2923a;
    --yellow: #f6c21a;
    --green: #3fae49;
    --blue: #2f7fcf;
    --pink-wash: #e58bc6;
    --peach-wash: #f7d8c4;
    --beige-wash: #e9c9a8;
    --cream: #fdf6ee;
    --dots: #555;
  }
  * { box-sizing: border-box; margin: 0; padding: 0; }
  html, body { width: 1200px; height: 1031px; overflow: hidden; background: var(--stage); }
  body { position: relative; font-family: "Jost", "Futura", sans-serif; color: var(--ink); }

  .invite { position: absolute; top: 120px; width: 395px; height: 705px; overflow: hidden; }
  .invite--watercolour { left: 120px;
    background: linear-gradient(180deg, #e38fc8 0%, #f3b7d6 25%, var(--peach-wash) 55%, #fdf1ea 80%, #fff 100%); }
  .invite--bokeh { left: 608px;
    background: radial-gradient(circle at 85% 10%, var(--beige-wash) 0%, transparent 45%),
                linear-gradient(180deg, #f1dcc6 0%, var(--cream) 55%, #fff 100%); }

  .el { position: absolute; }
  .rule { position: absolute; left: 50px; right: 50px; border-top: 2px dotted var(--dots); }
  .center { left: 0; right: 0; text-align: center; }

  .ribbon { position: absolute; }
  .ribbon svg { position: absolute; inset: 0; width: 100%; height: 100%; }
  .ribbon span { position: relative; display: flex; height: 100%; align-items: center; justify-content: center;
    color: #fff; font-weight: 700; white-space: nowrap; }

  .figures { position: absolute; border-radius: 40px;
    background: linear-gradient(90deg, #f6c21a 0%, #2f7fcf 30%, #e4262b 70%, #f6c21a 100%); opacity: .85; }
  .emoji-tear { position: absolute; border-radius: 50%; background: var(--yellow); border: 3px solid #e0a400; }

  .title { font-weight: 700; line-height: 1.2; letter-spacing: .3px; }
  .script { font-family: "Great Vibes", cursive; font-weight: 400; }
  .date { font-weight: 600; font-size: 16px; }

  .icon-tile { position: absolute; border: 3px solid; border-radius: 9px; background: #fff; }
  .icon-tile--red { border-color: var(--red); }
  .icon-tile--yellow { border-color: var(--yellow); }
  .icon-tile--green { border-color: var(--green); }
  .icon-tile .art { position: absolute; inset: 16px; border-radius: 6px; }
  .art--hat { background: linear-gradient(135deg, #f7d24a, #ec5a5a); }
  .art--thumb { background: linear-gradient(135deg, #5aa0e0, var(--blue)); }
  .art--cone { background: linear-gradient(180deg, #ec5fa5, #f3b744); }

  .rsvp { color: var(--red); font-weight: 700; font-size: 25px; }
  .rsvp-line { font-weight: 600; font-size: 13.5px; }
  .flourish { position: absolute; height: 14px; border-radius: 7px; background: linear-gradient(90deg, transparent, #777, transparent); opacity: .6; }
</style>
</head>
<body>

<section class="invite invite--watercolour" aria-label="Farewell dinner invitation, pink version">
  <div class="ribbon" style="left:17px; top:35px; width:355px; height:37px;">
    <svg viewBox="0 0 355 37" preserveAspectRatio="none" aria-hidden="true">
      <polygon points="0,0 355,0 343,18.5 355,37 0,37 12,18.5" fill="#1c1c1c"/>
    </svg>
    <span style="font-size:20px;">•&nbsp; DRESS IN YOUR BEST &nbsp;•</span>
  </div>
  <div class="figures" role="img" aria-label="Emoji of a boy in long pants and a girl in a dress holding hands" style="left:105px; top:88px; width:185px; height:195px;"></div>
  <div class="rule" style="top:294px;"></div>
  <div class="el title" style="left:65px; top:307px; font-size:20px;">FOR YOUR YEAR 6<br>FAREWELL DINNER</div>
  <div class="emoji-tear" role="img" aria-label="Crying face emoji" style="left:280px; top:306px; width:50px; height:50px;"></div>
  <div class="rule" style="top:368px;"></div>
  <div class="el" style="left:60px; top:383px; color:var(--red);"><span class="script" style="font-size:24px;">Hope u Can</span> <span class="title" style="font-size:20px;">MAKE IT....</span></div>
  <div class="el" style="left:168px; top:410px; color:var(--red);"><span class="script" style="font-size:24px;">Going to</span> <span class="title" style="font-size:20px;">BE GREAT</span></div>
  <div class="rule" style="top:448px;"></div>
  <div class="el center date" style="top:451px;">ON MONDAY 12 DECEMBER AT 6 PM</div>
  <div class="rule" style="top:482px;"></div>
  <div class="icon-tile icon-tile--red" style="left:57px; top:490px; width:80px; height:80px;"><div class="art art--hat" role="img" aria-label="Party hat emoji"></div></div>
  <div class="icon-tile icon-tile--yellow" style="left:155px; top:490px; width:80px; height:80px;"><div class="art art--thumb" role="img" aria-label="Thumbs up emoji"></div></div>
  <div class="icon-tile icon-tile--green" style="left:255px; top:490px; width:80px; height:80px;"><div class="art art--cone" role="img" aria-label="Ice cream emoji"></div></div>
  <div class="el center rsvp" style="top:587px;">RSVP</div>
  <div class="el center rsvp-line" style="top:624px;">Yes Please And Your Name To 0459XXXXXXX</div>
  <div class="flourish" role="img" aria-label="Decorative flourish" style="left:125px; top:661px; width:145px;"></div>
</section>

<section class="invite invite--bokeh" aria-label="Farewell dinner invitation, gold version">
  <div class="rule" style="top:42px; left:35px; right:35px;"></div>
  <div class="el center title" style="top:48px; font-size:30px;">DRESS IN YOUR BEST</div>
  <div class="rule" style="top:90px; left:35px; right:35px;"></div>
  <div class="figures" role="img" aria-label="Emoji of a boy in long pants and a girl in a dress holding hands" style="left:110px; top:102px; width:175px; height:188px;"></div>
  <div class="ribbon" style="left:15px; top:308px; width:360px; height:30px;">
    <svg viewBox="0 0 360 30" preserveAspectRatio="none" aria-hidden="true">
      <polygon points="0,15 10,0 350,0 360,15 350,30 10,30" fill="#c2923a"/>
    </svg>
    <span><span class="script" style="font-size:18px;">Hope u Can</span>&nbsp;<span style="font-size:15px;">MAKE IT.</span>&nbsp;<span class="script" style="font-size:18px;">Going to</span>&nbsp;<span style="font-size:15px;">BE GREAT</span></span>
  </div>
  <div class="el title" style="left:38px; top:362px; font-size:25px;">FOR YOUR YEAR 6</div>
  <div class="el title" style="left:38px; top:393px; font-size:25px; color:var(--gold);">FAREWELL DINNER</div>
  <div class="emoji-tear" role="img" aria-label="Crying face emoji" style="left:295px; top:362px; width:56px; height:56px;"></div>
  <div class="rule" style="top:440px; left:35px; right:35px;"></div>
  <div class="el center date" style="top:452px;">ON MONDAY 12 DECEMBER AT 6 PM</div>
  <div class="rule" style="top:483px; left:35px; right:35px;"></div>
  <div class="icon-tile icon-tile--red" style="left:45px; top:503px; width:88px; height:88px;"><div class="art art--hat" role="img" aria-label="Party hat emoji"></div></div>
  <div class="icon-tile icon-tile--yellow" style="left:152px; top:503px; width:88px; height:88px;"><div class="art art--thumb" role="img" aria-label="Thumbs up emoji"></div></div>
  <div class="icon-tile icon-tile--green" style="left:262px; top:503px; width:88px; height:88px;"><div class="art art--cone" role="img" aria-label="Ice cream emoji"></div></div>
  <div class="rule" style="top:620px; left:35px; right:35px;"></div>
  <div class="el center rsvp" style="top:623px;">RSVP</div>
  <div class="el center rsvp-line" style="top:660px;">Yes Please And Your Name To 0459XXXXXXX</div>
</section>

</body>
</html>
```